Flyer Frost Glow Cycle Tour
Zielgruppe
Wir sind DER Bikeshop in St. Moritz, welches auf 1800 m.ü.m. liegt. Wir verkaufen, vermieten uns servicen Bikes das ganze Jahr hindurch und haben auch 365 Tage im Jahr geöffnet. Wir sind die ersten, welche das Winterbiken für alle zugänglich gemacht haben und mit unseren Durafelt E-MTB ist das Fahren auf dem Schnee erstens sehr einfach und zweitens absolut sicher.
Aufgabenstellung
Flyerformat ist egal. Unsere Geschäftsfarben sind schwarz und gelb, der Hauptfont unseres Namens ist Marvelouz und wir arbeiten im High End Bereich. Gerne zwei Sprachen verwenden, evtl. Rückseite und Vorderseite gleich, nur die Sprachen ändern.
TEXT:
St. Moritz
Frost Glow Cycle Tour
Im Winter zu Biken ist ja schon verrückt, aber das ganze in der Nacht zu machen scheint ein Ding der Unmöglichkeit. Es ist das wahrscheinlich eines der coolsten Erlebnisse, welches es in St. Moritz im Winter gibt. Dank den Durafelt E-Bikes mit Spikes und unseren tollen Guides können Sie diese Ausfahrt auch sehr sicher erleben und sie ist für alle Personen, egal welchen Alters geeignet.
Auf speziellen Wunsch organisieren wir auch ein Outdoor-Abendessen, eine versteckte Alphütte zum Essen und Partymachen oder ganz einfach eine Champagnerpause im Pulverschnee dazu.
Dauer
1.5 – 2 Stunden
Inbegriffen
High End E-Bikes von Durafelt, Helm, Stirnlampe, heisses Getränk, Guide
Preis
ab Fr. 95.- pro Person (bei 8 Teilnehmern), Fr. 97.- bei 7 T., Fr. 100.- bei 6 T., Fr. 104.- bei 5 T., Fr. 110.- bei 4 T., Fr. 120.- bei 3 T., Fr. 140.- bei 2 T., Fr. 200.- bei einem Teilnemer.
Biking in winter is already crazy, but doing it at night seems impossible. It’s probably one of the coolest experiences you can have in St. Moritz in winter. Thanks to the Durafelt e-bikes with spikes and our great guides, you can also experience this ride very safely and it is suitable for all people, no matter what age.
On special request, we can also organise an outdoor dinner, a hidden alpine hut for eating and partying or simply a champagne break in the powder snow.
Duration
Included
High End E-Bikes von Durafelt, Helm, Stirnlampe, heisses Getränk, ..

```html
<!DOCTYPE html>
<html lang="de">
<head>
<meta charset="utf-8">
<title>Frost Glow Cycle Tour – Flyer</title>
<link rel="stylesheet" href="https://fonts.googleapis.com/css2?family=Rye&family=Poppins:wght@400;500;600;700&display=swap">
<style>
  :root {
    --canvas: #ebebeb;
    --ink-dark: #252525;
    --night: #1c2129;
    --brand-yellow: #f4c51c;
    --brand-blue: #1f3f7c;
    --paper: #ffffff;
    --text-light: #e9e9e9;
    --text-dark: #1d1d1d;
  }
  * { box-sizing: border-box; margin: 0; padding: 0; }
  html, body { width: 1200px; height: 800px; overflow: hidden; }
  body {
    background: var(--canvas);
    font-family: "Poppins", sans-serif;
    position: relative;
  }
  .flyer {
    position: absolute;
    top: 46px;
    width: 500px;
    height: 707px;
    background: var(--ink-dark);
    overflow: hidden;
    box-shadow: 0 10px 30px rgba(0,0,0,.18);
  }
  .flyer--en { left: 70px; }
  .flyer--de { left: 630px; }

  .night-backdrop {
    position: absolute; left: 0; top: 300px; width: 100%; height: 230px;
    background: linear-gradient(160deg, #2b2c30 0%, #34343a 45%, #1f2a36 100%);
  }
  .photo-fire {
    position: absolute; left: 285px; top: 0; width: 215px; height: 290px;
    border-left: 4px solid var(--paper);
    border-bottom: 4px solid var(--paper);
    border-bottom-left-radius: 60px;
    background: linear-gradient(180deg, #7fa4d4 0%, #a9c0de 30%, #d9c3b2 55%, #f0a04a 78%, #e4681c 100%);
  }
  .photo-riders {
    position: absolute; left: 12px; top: 330px; width: 196px; height: 182px;
    border: 4px solid var(--paper);
    border-radius: 22px;
    background: linear-gradient(170deg, #3d5470 0%, #54677c 40%, #c9c3a6 60%, #2a3848 100%);
    z-index: 3;
  }

  .brand {
    position: absolute; left: 32px; top: 32px;
    display: flex; align-items: center; gap: 8px;
    color: var(--paper);
    font-weight: 700; font-size: 15px; letter-spacing: 4px;
  }
  .brand__dot { width: 12px; height: 12px; border-radius: 50%; background: var(--paper); }

  .title {
    position: absolute; left: 32px; top: 88px;
    font-family: "Rye", serif;
    line-height: 1.18;
  }
  .title__place { color: var(--paper); font-size: 23px; display: block; }
  .title__tour { color: var(--brand-yellow); font-size: 26px; display: block; }

  .intro {
    position: absolute; left: 32px; top: 208px; width: 245px;
    color: var(--text-light); font-size: 8.4px; line-height: 1.6;
  }
  .intro .place { color: var(--brand-yellow); }
  .extras {
    position: absolute; left: 236px; top: 398px; width: 238px;
    color: var(--text-light); font-size: 8.6px; line-height: 1.6;
  }

  .duration-band {
    position: absolute; left: 0; top: 520px; width: 100%; height: 38px;
    background: var(--brand-blue);
    color: var(--paper);
    font-family: "Rye", serif; font-size: 17px;
    display: flex; align-items: center; justify-content: flex-end;
    padding-right: 22px;
  }

  .offer {
    position: absolute; left: 0; top: 558px; width: 100%; height: 118px;
    background: var(--brand-yellow);
    display: flex; align-items: center;
    padding: 0 16px 0 28px;
  }
  .included {
    width: 118px; padding-right: 12px;
    border-right: 1px solid var(--brand-blue);
    font-size: 9.6px; line-height: 1.35; color: var(--text-dark);
  }
  .included__label { color: var(--brand-blue); font-weight: 600; display: block; margin-bottom: 2px; }
  .prices {
    flex: 1;
    display: grid; grid-template-columns: repeat(4, 1fr); row-gap: 8px;
    padding-left: 10px;
  }
  .price { text-align: center; color: var(--text-dark); font-size: 7px; line-height: 1.25; }
  .price__amount { font-family: "Rye", serif; color: var(--brand-blue); font-size: 17px; line-height: 1.1; display: block; }
  .price__currency { font-size: 9px; }

  .contact-bar {
    position: absolute; left: 0; top: 676px; width: 100%; height: 31px;
    background: var(--paper);
    display: flex; align-items: center; justify-content: space-around;
    padding: 0 14px;
    font-size: 7.6px; font-weight: 600; color: var(--text-dark);
  }
  .contact { display: flex; align-items: center; gap: 4px; }
  .contact svg { width: 10px; height: 10px; fill: none; stroke: var(--brand-blue); stroke-width: 2; }
  .icons { position: absolute; width: 0; height: 0; }
</style>
</head>
<body>

<svg class="icons" aria-hidden="true">
  <symbol id="icon-pin" viewBox="0 0 24 24"><path d="M12 22s7-7 7-12a7 7 0 0 0-14 0c0 5 7 12 7 12z"/><circle cx="12" cy="10" r="2.5"/></symbol>
  <symbol id="icon-phone" viewBox="0 0 24 24"><path d="M5 3h4l2 5-3 2a12 12 0 0 0 6 6l2-3 5 2v4a2 2 0 0 1-2 2A18 18 0 0 1 3 5a2 2 0 0 1 2-2z"/></symbol>
  <symbol id="icon-mail" viewBox="0 0 24 24"><rect x="3" y="5" width="18" height="14" rx="1"/><path d="M3 6l9 7 9-7"/></symbol>
  <symbol id="icon-globe" viewBox="0 0 24 24"><circle cx="12" cy="12" r="9"/><path d="M3 12h18M12 3c3 3 3 15 0 18M12 3c-3 3-3 15 0 18"/></symbol>
</svg>

<!-- English side -->
<article class="flyer flyer--en" lang="en">
  <div class="night-backdrop" role="img" aria-label="Dark photo of riders with headlamps on fat e-bikes in the snow"></div>
  <div class="photo-fire" role="img" aria-label="Photo of a guide beside a glowing fire bowl in the snow at dusk"></div>
  <div class="photo-riders" role="img" aria-label="Photo of riders on e-bikes under lit snowy trees at night"></div>

  <div class="brand"><span class="brand__dot"></span>TRAILHAUS</div>
  <h1 class="title">
    <span class="title__place">ST. MORITZ</span>
    <span class="title__tour">FROST GLOW</span>
    <span class="title__tour">CYCLE TOUR</span>
  </h1>
  <p class="intro">Biking in winter is already crazy, but doing it at night seems impossible. It’s probably one of the coolest experiences you can have in <span class="place">St. Moritz</span> in winter. Thanks to the Durafelt e-bikes with spikes and our great guides, you can also experience this ride very safely and it is suitable for all people, no matter what age.</p>
  <p class="extras">On special request, we can also organise an outdoor dinner, a hidden alpine hut for eating and partying or simply a champagne break in the powder snow.</p>

  <div class="duration-band">DURATION: 1.5-2 HOURS</div>

  <section class="offer">
    <p class="included"><span class="included__label">Included:</span>High End E-Bikes von Durafelt, Helm, Stirnlampe, heisses Getränk, Guide</p>
    <div class="prices">
      <p class="price"><span class="price__amount"><span class="price__currency">FR.</span>95.-</span>per person<br>(with 8 participants)</p>
      <p class="price"><span class="price__amount"><span class="price__currency">FR.</span>97.-</span>per person<br>(with 7 participants)</p>
      <p class="price"><span class="price__amount"><span class="price__currency">FR.</span>100.-</span>per person<br>(with 6 participants)</p>
      <p class="price"><span class="price__amount"><span class="price__currency">FR.</span>104.-</span>per person<br>(with 5 participants)</p>
      <p class="price"><span class="price__amount"><span class="price__currency">FR.</span>110.-</span>per person<br>(with 4 participants)</p>
      <p class="price"><span class="price__amount"><span class="price__currency">FR.</span>120.-</span>per person<br>(with 3 participants)</p>
      <p class="price"><span class="price__amount"><span class="price__currency">FR.</span>140.-</span>per person<br>(with 2 participants)</p>
      <p class="price"><span class="price__amount"><span class="price__currency">FR.</span>200.-</span>per person<br>(with 1 participant)</p>
    </div>
  </section>

  <footer class="contact-bar">
    <span class="contact"><svg><use href="#icon-pin"/></svg>Via Serlas 14 7500 St. Moritz</span>
    <span class="contact"><svg><use href="#icon-phone"/></svg>+41 81 555 01 23</span>
    <span class="contact"><svg><use href="#icon-mail"/></svg>stmoritz@trailhaus.ch</span>
    <span class="contact"><svg><use href="#icon-globe"/></svg>www.trailhaus.ch</span>
  </footer>
</article>

<!-- German side -->
<article class="flyer flyer--de">
  <div class="night-backdrop" role="img" aria-label="Dunkles Foto von Fahrern mit Stirnlampen auf Fatbikes im Schnee"></div>
  <div class="photo-fire" role="img" aria-label="Foto eines Guides neben einer glühenden Feuerschale im Schnee"></div>
  <div class="photo-riders" role="img" aria-label="Foto von E-Bike-Fahrern unter beleuchteten verschneiten Bäumen"></div>

  <div class="brand"><span class="brand__dot"></span>TRAILHAUS</div>
  <h1 class="title">
    <span class="title__place">ST. MORITZ</span>
    <span class="title__tour">FROST GLOW</span>
    <span class="title__tour">CYCLE TOUR</span>
  </h1>
  <p class="intro">Im Winter zu Biken ist ja schon verrückt, aber das ganze in der Nacht zu machen scheint ein Ding der Unmöglichkeit. Es ist das wahrscheinlich eines der coolsten Erlebnisse, welches es in <span class="place">St. Moritz</span> im Winter gibt. Dank den Durafelt E-Bikes mit Spikes und unseren tollen Guides können Sie diese Ausfahrt auch sehr sicher erleben und sie ist für alle Personen, egal welchen Alters geeignet.</p>
  <p class="extras">Auf speziellen Wunsch organisieren wir auch ein Outdoor-Abendessen, eine versteckte Alphütte zum Essen und Partymachen oder ganz einfach eine Champagnerpause im Pulverschnee dazu.</p>

  <div class="duration-band">DAUER: 1.5-2 STUNDEN</div>

  <section class="offer">
    <p class="included"><span class="included__label">Inbegriffen:</span>High End E-Bikes von Durafelt, Helm, Stirnlampe, heisses Getränk, Guide</p>
    <div class="prices">
      <p class="price"><span class="price__amount"><span class="price__currency">FR.</span>95.-</span>pro Person<br>(bei 8 Teilnehmern)</p>
      <p class="price"><span class="price__amount"><span class="price__currency">FR.</span>97.-</span>pro Person<br>(bei 7 Teilnehmern)</p>
      <p class="price"><span class="price__amount"><span class="price__currency">FR.</span>100.-</span>pro Person<br>(bei 6 Teilnehmern)</p>
      <p class="price"><span class="price__amount"><span class="price__currency">FR.</span>104.-</span>pro Person<br>(bei 5 Teilnehmern)</p>
      <p class="price"><span class="price__amount"><span class="price__currency">FR.</span>110.-</span>pro Person<br>(bei 4 Teilnehmern)</p>
      <p class="price"><span class="price__amount"><span class="price__currency">FR.</span>120.-</span>pro Person<br>(bei 3 Teilnehmern)</p>
      <p class="price"><span class="price__amount"><span class="price__currency">FR.</span>140.-</span>pro Person<br>(bei 2 Teilnehmern)</p>
      <p class="price"><span class="price__amount"><span class="price__currency">FR.</span>200.-</span>pro Person<br>(bei 1 Teilnehmer)</p>
    </div>
  </section>

  <footer class="contact-bar">
    <span class="contact"><svg><use href="#icon-pin"/></svg>Via Serlas 14 7500 St. Moritz</span>
    <span class="contact"><svg><use href="#icon-phone"/></svg>+41 81 555 01 23</span>
    <span class="contact"><svg><use href="#icon-mail"/></svg>stmoritz@trailhaus.ch</span>
    <span class="contact"><svg><use href="#icon-globe"/></svg>www.trailhaus.ch</span>
  </footer>
</article>

</body>
</html>
```